WTF!!! We need a modern professional website for a business litigation law firm.

We need a modern, clean, professional and uncomplicated website for a new business trial and litigation law firm called "Hallorand Trial Firm PLLC". Website must be mobile optimized for iPad and smartphone. The law firm specializes in counseling and representing large corporations, small businesses and entrepreneurs in and out of the courtroom. Lawyers in the firm serve as Florida counsel and trial counsel to organizations facing claims involving product liability, premises liability, professional liability, vehicle and transportation liability, warranty claims, construction defects and delay claims, complex business disputes, commercial litigation and bid disputes in State and Federal Courts. The website is mainly to provide information about the firm, and should include sections describing the firm, identifying the Industries Served and Areas of Practice ," a separate page identifying the "Professionals", a separate page for "Resources & Advisories," and a traveling "Connect With Us" button a site visitor can click on that will launch an email to the Firm's general email account. The website should allow us to easily modify the content on these pages, and let us add/modify links to external information sources. We will not sell anything or take payments through the website. We do need to be able to easily upload and update photographs of attorneys and add new attorneys names/email hyperlinks as the firm grows. We would like to add developments in the law or success stories easily and quickly, such as through a blog page. On the "Connect With Us" page the website should have hyperlinks to email the Firm, and there should be hyperlinks to email each professional on the "Professionals" page. The website should be viewable on mobile devices without distortion. The law firm focuses on trial work and should have some imagery associated with courtrooms, but the overall theme of the site should be modern, clean, and communicate sophistication and strength. The website should be made in Wordpress. We have uploaded logo files for Hallorand Trial Firm.

Target Market(s)

Corporations and companies that are looking for legal representation. Other attorneys/legal industry.

Industry/Entity Type

Legal Industry

Coding

Coded - Design and coding required

Number of Pages Required

1 page

Font styles to use
Sans Serif

Requirements
Must have
• Simple, clean, sophisticated, modern website that includes the logo, watermark of logo, and the elements described above.
Nice to have
• Pictures of city scape, buildings, courtroom, team members.

```html
<!DOCTYPE html>
<html lang="en">
<head>
<meta charset="utf-8">
<title>Hallorand Trial Firm PLLC</title>
<link rel="stylesheet" href="https://fonts.googleapis.com/css2?family=Poppins:wght@300;400;500;600;700;800&family=Lato:wght@400;700&family=Playfair+Display:wght@400&display=swap">
<style>
:root{
  --accent:#c8834b;
  --navy:#34304a;
  --navy-light:#3d3856;
  --ink:#2f2b44;
  --muted:#6b6878;
  --topbar:#f2f2f2;
  --white:#ffffff;
}
*{box-sizing:border-box;margin:0;padding:0}
html,body{width:1200px;height:4594px;overflow:hidden}
body{position:relative;background:var(--white);font-family:'Poppins',sans-serif;color:var(--ink)}
.abs{position:absolute}
.eyebrow{font-family:'Poppins',sans-serif;font-size:17px;letter-spacing:1.5px;color:var(--accent);font-weight:500;text-transform:uppercase}
.btn{position:absolute;background:var(--accent);color:var(--white);font-size:13px;font-weight:500;letter-spacing:.6px;text-transform:uppercase;display:flex;align-items:center;justify-content:center;border-radius:3px}

/* top bar */
.topbar{left:0;top:0;width:1200px;height:50px;background:var(--topbar);font-size:13px;font-weight:500}
.topbar .hours{left:37px;top:0;height:50px;display:flex;align-items:center;gap:10px}
.topbar .social{right:37px;top:0;height:50px;display:flex;align-items:center;gap:32px}
.topbar .social span{width:10px;height:10px;border-radius:50%;background:var(--ink)}

/* header */
.header{left:0;top:50px;width:1200px;height:98px;background:var(--white)}
.brand{left:37px;top:0;height:98px;display:flex;align-items:center;gap:10px;font-weight:700;font-size:20px;color:#111}
.brand i{display:block;width:18px;height:18px;background:#111}
.nav{left:498px;top:0;height:98px;display:flex;align-items:center;gap:42px;font-size:15px;color:var(--ink)}
.nav a{color:inherit;text-decoration:none}
.nav .active{color:var(--muted)}
.header .btn{left:1013px;top:19px;width:148px;height:54px}

/* hero */
.hero{left:0;top:148px;width:1200px;height:930px;background:linear-gradient(100deg,#1a1c1a 0%,#2a2f2a 40%,#4a4e48 62%,#d9d6d0 76%,#5b5750 100%)}
.hero .eyebrow{left:37px;top:186px;font-size:25px;font-weight:400}
.hero h1{left:37px;top:244px;font-size:88px;line-height:90px;font-weight:800;color:var(--white);letter-spacing:-.5px}
.hero p{left:37px;top:553px;width:525px;font-family:'Lato',sans-serif;font-size:15px;line-height:23.5px;color:#e6e6e6}
.hero .btn{left:37px;top:687px;width:185px;height:55px}

/* industries */
.industries{left:0;top:1078px;width:1200px;height:276px;background:var(--navy);display:flex;padding:0 23px}
.industry{flex:1;display:flex;flex-direction:column;align-items:center;padding-top:62px;color:var(--white);font-size:20px;line-height:26px;text-align:center}
.industry svg{width:84px;height:84px;margin-bottom:20px}

/* about */
.about-photo{left:37px;top:1643px;width:496px;height:471px;border-radius:6px;background:linear-gradient(135deg,#d8d6d2,#8c7e6e 50%,#3a3836)}
.about .eyebrow{left:628px;top:1640px}
.about h2{left:628px;top:1676px;width:540px;font-size:33px;line-height:42px;font-weight:600;color:var(--ink)}
.about p{left:628px;width:540px;font-family:'Lato',sans-serif;font-size:13px;line-height:24px;color:var(--muted)}
.about .btn{left:628px;top:1997px;width:154px;height:43px}

/* mission */
.col h3{font-size:32px;line-height:36px;font-weight:600;color:var(--ink)}
.col p{font-size:13.5px;line-height:24px;color:var(--muted)}
.col h4{font-size:25px;font-weight:600;color:var(--ink)}
.icon-box{width:70px;height:70px;background:var(--accent);border-radius:3px;display:flex;align-items:center;justify-content:center}
.mission-photo{left:399px;top:2235px;width:404px;height:478px;background:linear-gradient(90deg,#1c1a19,#4c3d32 45%,#8e8273 55%,#1e1c1b)}

/* help */
.help{left:0;top:2990px;width:1200px;height:545px;background:var(--navy);overflow:hidden}
.help svg.curve{position:absolute;left:0;top:0}
.help .eyebrow{left:0;width:1200px;text-align:center;top:194px}
.help h2{left:0;width:1200px;top:250px;text-align:center;font-size:46px;line-height:62px;font-weight:500;color:var(--white)}
.card{top:3441px;width:354px;height:286px;border-radius:6px;overflow:hidden}
.card .cap{position:absolute;left:23px;bottom:26px;color:var(--white)}
.card .cap b{display:block;font-size:26px;font-weight:600;margin-bottom:10px}
.card .cap span{font-size:15px;font-weight:500}
.arrow{top:3782px;width:45px;height:45px;background:var(--navy);border-radius:3px;display:flex;align-items:center;justify-content:center}

/* results */
.results .eyebrow{left:0;width:1200px;text-align:center;top:3995px}
.results h2{left:0;width:1200px;top:4058px;text-align:center;font-size:46px;line-height:62px;font-weight:500;color:var(--ink)}
.stat{top:4230px;width:300px;text-align:center}
.stat b{display:block;font-family:'Playfair Display',serif;font-weight:400;font-size:82px;line-height:100px;color:var(--accent)}
.stat span{font-size:19px;color:var(--ink)}
.results .btn{left:529px;top:4396px;width:142px;height:44px}
</style>
</head>
<body>

<div class="abs topbar">
  <div class="abs hours">
    <svg width="20" height="20" viewBox="0 0 20 20" fill="none" stroke="#6b6878" stroke-width="1.5"><circle cx="10" cy="10" r="8"/><path d="M10 5v5l3 2"/></svg>
    Mon - Fri 10:00-18:00
  </div>
  <div class="abs social"><span></span><span></span><span></span></div>
</div>

<header class="abs header">
  <div class="abs brand"><i></i>Hallorand</div>
  <nav class="abs nav">
    <a class="active">Home</a><a>Practice Areas</a><a>Attorney</a><a>Advisories</a><a>Blog</a>
  </nav>
  <div class="btn">Contact Us</div>
</header>

<section class="abs hero" role="img" aria-label="Attorney in a white shirt working on a laptop in a dark office"></section>
<div class="hero">
  <div class="abs eyebrow" style="top:334px">Counsel Law Firm</div>
  <h1 class="abs" style="top:392px">Best Law<br>Firm Since<br>2015</h1>
  <p class="abs" style="top:697px">At Hallorand Trial Firm, we've been providing trusted counsel to businesses and individuals for over 10 years. Our focus on strategic legal solutions ensures that we handle even the most complex matters with precision and dedication.</p>
  <div class="btn" style="top:834px">Legal Services</div>
</div>

<section class="abs industries">
  <div class="industry">
    <svg viewBox="0 0 84 84" fill="none" stroke="#fff" stroke-width="2.2" stroke-linejoin="round"><rect x="30" y="14" width="26" height="14" transform="rotate(40 43 21)"/><path d="M38 32 L16 56 M14 66h28"/></svg>
    Manufacturing
  </div>
  <div class="industry">
    <svg viewBox="0 0 84 84" fill="none" stroke="#fff" stroke-width="2.2" stroke-linejoin="round"><path d="M10 40 L42 10 L74 40 M18 34v42h48V34"/><path d="M32 56 L50 38 M44 32l12 12"/></svg>
    Construction &amp;<br>Real Estate
  </div>
  <div class="industry">
    <svg viewBox="0 0 84 84" fill="none" stroke="#fff" stroke-width="2.2" stroke-linejoin="round"><rect x="12" y="40" width="40" height="24"/><path d="M52 48h12l8 8v8H52"/><circle cx="24" cy="68" r="5"/><circle cx="60" cy="68" r="5"/><path d="M36 32 L52 18 M46 14l10 10"/></svg>
    Transportation
  </div>
  <div class="industry">
    <svg viewBox="0 0 84 84" fill="none" stroke="#fff" stroke-width="2.2" stroke-linejoin="round"><path d="M36 22 L14 30v16c0 14 10 22 22 28 12-6 22-14 22-28V30z"/><circle cx="62" cy="18" r="6"/><path d="M54 74V34h16v40"/></svg>
    Professional<br>Liability
  </div>
  <div class="industry">
    <svg viewBox="0 0 84 84" fill="none" stroke="#fff" stroke-width="2.2" stroke-linejoin="round"><path d="M22 12h30l10 10v50H22z"/><circle cx="54" cy="58" r="10"/><path d="M30 26h20M30 34h20M30 42h14"/></svg>
    Retail
  </div>
  <div class="industry">
    <svg viewBox="0 0 84 84" fill="none" stroke="#fff" stroke-width="2.2" stroke-linejoin="round"><rect x="14" y="14" width="56" height="44"/><path d="M34 58v12h16V58M26 70h32M42 22v26M30 30h24M30 30l-5 10h10zM54 30l-5 10h10z"/></svg>
    Technology &amp;<br>Startups
  </div>
</section>

<div class="about">
  <div class="abs about-photo" role="img" aria-label="Lawyer in a grey suit signing documents at a desk"></div>
  <div class="abs eyebrow">About Us</div>
  <h2 class="abs">Welcome To The Counsel Law Firm</h2>
  <p class="abs" style="top:1784px">wonderful serenity has taken possession of my entire soul, like these sweet mornings of spring which I enjoy with my whole heart.A wonderful serenity has taken possession of my entire soul, like these sweet mornings of spring which I enjoy with my whole heart.</p>
  <p class="abs" style="top:1912px">wonderful serenity has taken possession of my entire soul, like these sweet mornings of spring which I enjoy with my whole heart</p>
  <div class="btn">Read More</div>
</div>

<div class="col">
  <div class="abs eyebrow" style="left:43px;top:2240px">Our Mission</div>
  <h3 class="abs" style="left:43px;top:2278px;width:340px">We're Recognized In All Legal Practises</h3>
  <p class="abs" style="left:43px;top:2364px;width:320px">Excellence Across All Legal Practices. Trusted. Proven Respected a Legacy of Success in Every Area of Law We Practice.</p>
  <div class="abs icon-box" style="left:43px;top:2500px"><svg width="34" height="34" viewBox="0 0 34 34" fill="none" stroke="#fff" stroke-width="1.8"><path d="M17 3 L5 8v9c0 7 5 11 12 14 7-3 12-7 12-14V8z"/><circle cx="17" cy="16" r="5"/></svg></div>
  <h4 class="abs" style="left:43px;top:2580px">Trusted Law Firm</h4>
  <p class="abs" style="left:43px;top:2626px;width:320px">Your Trusted Legal Partner in Every Challenge. Trust integrity, Excellence in Litigation and Business Law</p>
</div>
<div class="abs mission-photo" role="img" aria-label="Library hall with tall bookshelves and marble busts"></div>
<div class="col">
  <div class="abs eyebrow" style="left:830px;top:2240px">Why Choose Us</div>
  <h3 class="abs" style="left:830px;top:2278px;width:340px">We solve Complex legal issues</h3>
  <p class="abs" style="left:830px;top:2364px;width:340px">Experience. Strategy. Solutions for Complex Legal Matters turning Legal Challenges into Legal Victories</p>
  <div class="abs icon-box" style="left:830px;top:2500px"><svg width="34" height="34" viewBox="0 0 34 34" fill="none" stroke="#fff" stroke-width="1.8"><rect x="4" y="10" width="26" height="18" rx="2"/><path d="M12 10V6h10v4M4 17h26M15 17v3h4v-3"/></svg></div>
  <h4 class="abs" style="left:830px;top:2580px">Find Best Lawyers</h4>
  <p class="abs" style="left:830px;top:2626px;width:340px">Find the Right Lawyers. Get the Best Results. Elite advocacy trusted Counsel and Outstanding Results</p>
</div>

<section class="abs help">
  <svg class="curve" width="1200" height="545" viewBox="0 0 1200 545"><path d="M0 100 C40 200 120 330 360 390 C600 450 820 430 1200 545 L0 545Z" fill="#3b3752"/></svg>
  <div class="abs eyebrow">How We Can Help</div>
  <h2 class="abs">Meeting the needs of our clients<br>since 2015.</h2>
</section>
<div class="abs card" style="left:37px;background:linear-gradient(160deg,#2c2846,#6b5a4a 55%,#1d1a22)" role="img" aria-label="Scales of justice and gavel">
  <div class="cap"><b>Product Liability</b><span>Defending Product Liability Claims</span></div>
</div>
<div class="abs card" style="left:424px;background:linear-gradient(160deg,#c9b8a4,#7a3a26 45%,#3d1c14)" role="img" aria-label="Row of law books">
  <div class="cap"><b>Transportation Liability</b><span>Protecting Against Vehicle Claims</span></div>
</div>
<div class="abs card" style="left:810px;background:linear-gradient(160deg,#cfd8e2,#6e8fb4 50%,#2f3f5a)" role="img" aria-label="Businessman in a blue shirt looking out a window">
  <div class="cap"><b>Warranty Claims</b><span>Protecting Against Warranty Claims</span></div>
</div>
<div class="abs arrow" style="left:549px"><svg width="12" height="12" viewBox="0 0 12 12" fill="none" stroke="#fff" stroke-width="1.6"><path d="M8 1L3 6l5 5"/></svg></div>
<div class="abs arrow" style="left:606px"><svg width="12" height="12" viewBox="0 0 12 12" fill="none" stroke="#fff" stroke-width="1.6"><path d="M4 1l5 5-5 5"/></svg></div>

<section class="results">
  <div class="abs eyebrow">Our Results</div>
  <h2 class="abs">Our Firm Is One Of The Most<br>Successful Law Firms</h2>
  <div class="abs stat" style="left:94px"><b>88%</b><span>Cases Solved</span></div>
  <div class="abs stat" style="left:450px"><b>6k</b><span>Happy Clients</span></div>
  <div class="abs stat" style="left:806px"><b>96%</b><span>Successful Tasks</span></div>
  <div class="btn">About Us</div>
</section>

</body>
</html>
```